Esoteric, wellness company labels

Verdant Lumen is a lifestyle brand with multiple products. We have an offshoot as well called Lumen Coffee. I need multiple labels or packaging designs that all match so I can start wholesaling.

I want something fun and very eye catching. I have two different logos for Verdant Lumen but just one for the coffee. I’m
Undecided which one I want on the labels because I like both. So either would work. Any coffee products go under lumen coffee and any other products go under Verdant Lumen.

We sell items such as crystals, tarot and oracle decks, candles, organic coffee, superfood powders and herbs and more.

The items I need labels for should have a streamline look so that all are recognizable as the Verdant Lumen brand. The products that are a priority are:
Organic coffee
Reishi infused coffee
Lion’s Mane infused coffee
Those go under Lumen Coffee.

Soon I’ll do more items;
Sacred smudging spray
Sacred smudging cleaner
Multiple superfoods
Etc
Updates

We have decided to use compostable coffee bags that are approximately 9x6x33cm so your standard 1lb bag you would see in a store. We still want colorful and eye catching but at the same time being eco friendly. The coffee is 100% organic, free trade, low acid.

We are looking for labels for the coffee but also want to be able to use the same kind of design or similar down the road for our other products. We carry superfood powders (lion’s mane, blue Spirulina, reishi, pearl powder, sea moss etc) but also things like smudging spray, rose water, neroli water, essential oils etc. we are a lifestyle company so we are looking for labels across our store brand items.

Target Market(s)

Esoteric, health and wellness, “new age”

Industry/Entity Type

Retail, wellness,

Colors

Designer to choose colors to be used in the design.

Requirements
Must have
• Beauty, attraction
Should not have
• Anything to do with religion, no dark witchy themes

```html
<!DOCTYPE html>
<html lang="en">
<head>
<meta charset="utf-8">
<title>Verdant Lumen – Pouch Label</title>
<link rel="stylesheet" href="https://fonts.googleapis.com/css2?family=Gloock&family=Mrs+Saint+Delafield&family=Montserrat:wght@500&display=swap">
<style>
  :root {
    --backdrop: #8e8e8e;
    --pouch-white: #f7f7f5;
    --ink-navy: #1d2340;
    --terracotta: #b45a40;
    --photo-deep: #3a2a26;
    --photo-warm: #8a4a36;
  }
  html, body {
    margin: 0;
    padding: 0;
    width: 1200px;
    height: 1199px;
    overflow: hidden;
    background: var(--backdrop);
  }
  .pouch-front {
    position: absolute;
    left: 287px;
    top: 50px;
    width: 626px;
    height: 1100px;
    background: var(--pouch-white);
    border-radius: 14px;
    overflow: hidden;
    color: var(--ink-navy);
    text-align: center;
  }
  .brand-dot {
    position: absolute;
    left: 50%;
    top: 130px;
    width: 70px;
    height: 70px;
    margin-left: -35px;
    border-radius: 50%;
    background: var(--ink-navy);
  }
  .brand-name {
    position: absolute;
    left: 0;
    right: 0;
    top: 268px;
    margin: 0;
    font-family: "Gloock", serif;
    font-weight: 400;
    font-size: 66px;
    line-height: 60px;
    letter-spacing: 1px;
    text-transform: uppercase;
  }
  .brand-tagline {
    position: absolute;
    left: 0;
    right: 0;
    top: 408px;
    margin: 0;
    font-family: "Mrs Saint Delafield", cursive;
    font-size: 40px;
  }
  .product-pillars {
    position: absolute;
    left: 0;
    right: 0;
    top: 480px;
    margin: 0;
    font-family: "Mrs Saint Delafield", cursive;
    font-size: 18px;
    word-spacing: 38px;
  }
  .web-address {
    position: absolute;
    left: 0;
    right: 0;
    top: 506px;
    margin: 0;
    font-family: "Montserrat", sans-serif;
    font-weight: 500;
    font-size: 7px;
    letter-spacing: 3px;
    text-transform: uppercase;
  }
  .lower-art {
    position: absolute;
    left: 0;
    top: 560px;
    width: 626px;
    height: 540px;
  }
</style>
</head>
<body>
  <main class="pouch-front">
    <span class="brand-dot"></span>
    <h1 class="brand-name">Verdant<br>Lumen</h1>
    <p class="brand-tagline">metaphysical boutique</p>
    <p class="product-pillars">lifestyle health beauty</p>
    <p class="web-address">www.verdantlumen.com</p>

    <svg class="lower-art" viewBox="0 0 626 540" xmlns="http://www.w3.org/2000/svg">
      <defs>
        <linearGradient id="boutique-tones" x1="0" y1="0" x2="0.4" y2="1">
          <stop offset="0" stop-color="var(--photo-deep)"/>
          <stop offset="0.5" stop-color="var(--photo-warm)"/>
          <stop offset="1" stop-color="var(--photo-deep)"/>
        </linearGradient>
      </defs>
      <rect class="terracotta-band" x="0" y="105" width="626" height="435" fill="var(--terracotta)"/>
      <circle class="boutique-photo" cx="313" cy="300" r="290" fill="url(#boutique-tones)"
              role="img" aria-label="Photo of the boutique interior: terracotta cushions on a chair, plants, checkered floor and a wooden table"/>
    </svg>
  </main>
</body>
</html>
```